Interior designer needs a gorgeous, chic business card design.

A new, small Interior Design firm needs a business card that is chic, contemporary and elegant. Nothing over the top. My interiors are contemporary classic with an elegant feel to them. I like to use quality finishes and products rather than follow the latest fads. Projects can be anything from Pre start selections, bathrooms, kitchens, bedrooms, custom upholstery, furniture, rugs and art etc. The final design should display quality and an achievable sense of chic. I am open to all colours including black but not limited to this.

```html
<!DOCTYPE html>
<html lang="en">
<head>
<meta charset="utf-8">
<title>Vela Interiors – Business Card</title>
<link href="https://fonts.googleapis.com/css2?family=Bodoni+Moda:wght@400;600&display=swap" rel="stylesheet">
<style>
  :root {
    --backdrop: #b48f89;
    --gold-light: #f3df9c;
    --gold-mid: #e9cb83;
    --gold-deep: #d7ae66;
    --paper: #ffffff;
    --ink: #141210;
    --ink-soft: #4f4a42;
  }
  * { margin: 0; padding: 0; box-sizing: border-box; }
  html, body {
    width: 1200px;
    height: 1200px;
    overflow: hidden;
  }
  body {
    position: relative;
    background: var(--backdrop);
    font-family: "Bodoni Moda", "Didot", serif;
    color: var(--ink);
  }
  .gold {
    background: linear-gradient(160deg, var(--gold-light) 0%, var(--gold-mid) 45%, var(--gold-deep) 100%);
  }

  /* Front of card */
  .card-front {
    position: absolute;
    left: 268px;
    top: 177px;
    width: 655px;
    height: 358px;
    background: var(--paper);
  }
  .card-front__face {
    position: absolute;
    left: 29px;
    top: 22px;
    width: 597px;
    height: 314px;
    display: flex;
    align-items: center;
    justify-content: center;
  }
  .brand-front {
    font-size: 52px;
    font-weight: 400;
    letter-spacing: 2px;
    line-height: 1;
    color: var(--paper);
    white-space: nowrap;
  }

  /* Back of card */
  .card-back {
    position: absolute;
    left: 268px;
    top: 685px;
    width: 655px;
    height: 358px;
  }
  .card-back__frame {
    position: absolute;
    left: 26px;
    top: 21px;
    width: 604px;
    height: 316px;
    border: 2px solid var(--paper);
  }
  .brand-back {
    position: absolute;
    left: 44px;
    top: 50px;
    font-size: 30px;
    font-weight: 400;
    letter-spacing: 1px;
    line-height: 1;
    color: var(--ink);
    white-space: nowrap;
  }
  .contact-person {
    position: absolute;
    right: 40px;
    top: 42px;
    text-align: right;
    line-height: 1;
  }
  .contact-person__name {
    font-size: 25px;
    font-weight: 600;
    color: var(--ink);
  }
  .contact-person__qual {
    margin-top: 10px;
    font-size: 20px;
    color: var(--ink-soft);
  }
  .contact-person__role {
    margin-top: 9px;
    font-size: 20px;
    color: var(--ink-soft);
  }
  .contact-list {
    position: absolute;
    left: 0;
    top: 178px;
    width: 100%;
    list-style: none;
  }
  .contact-list__item {
    height: 61px;
    font-size: 20px;
    color: var(--ink-soft);
    display: flex;
    justify-content: center;
    align-items: flex-start;
    gap: 8px;
  }
  .contact-list__icon {
    width: 22px;
    height: 22px;
    margin-top: 2px;
    fill: none;
    stroke: var(--ink-soft);
    stroke-width: 1.6;
  }
</style>
</head>
<body>

  <section class="card-front">
    <div class="card-front__face gold">
      <p class="brand-front">VELA INTERIORS</p>
    </div>
  </section>

  <section class="card-back gold">
    <div class="card-back__frame"></div>

    <p class="brand-back">VELA INTERIORS</p>

    <div class="contact-person">
      <p class="contact-person__name">Mirela Voss Hart</p>
      <p class="contact-person__qual">(Dip. Interior Design)</p>
      <p class="contact-person__role">Director</p>
    </div>

    <ul class="contact-list">
      <li class="contact-list__item">
        <svg class="contact-list__icon" viewBox="0 0 24 24" aria-hidden="true">
          <rect x="2" y="6" width="20" height="13"/>
          <path d="M2 6 L12 14 L22 6"/>
        </svg>
        <span>mirela@velainteriors.com.au</span>
      </li>
      <li class="contact-list__item">
        <svg class="contact-list__icon" viewBox="0 0 24 24" aria-hidden="true">
          <rect x="6" y="2" width="12" height="20" rx="1.5"/>
          <rect x="8.5" y="5" width="7" height="12"/>
        </svg>
        <span>0400318264</span>
      </li>
      <li class="contact-list__item">
        <svg class="contact-list__icon" viewBox="0 0 24 24" aria-hidden="true">
          <circle cx="12" cy="12" r="9"/>
          <path d="M3 12 H21 M5 7.5 H19 M5 16.5 H19"/>
        </svg>
        <span>www.velainteriors.com</span>
      </li>
    </ul>
  </section>

</body>
</html>
```